Business Card Design

We need a business card for a well established Semi Trailer Hire company. I am looking for a new start as we are moving so would like to update our Business Cards and Letter heads.
We hire Semi Trailers to Transport companies.
The colour of our Trailers are Cherry Red so this must be the prominent colour.
I do not want any pictures of trailers on the design.
I do not want the design to be flowery in anyway as we are in the transport industry.
Simple yet effective

Business

Varno Tolt Hire Pty Ltd
Ros Penbury
Director
Ph: 03 9412 5038
Mobile: 0427 836 207
ros.penbury@varnotolt-example.com.au
www.varnotolt-example.com.au
218-224 Dunmore Road, Yarraville

```html
<!DOCTYPE html>
<html lang="en">
<head>
<meta charset="utf-8">
<title>Varno Tolt Hire Pty Ltd — Business Card</title>
<link rel="stylesheet" href="https://fonts.googleapis.com/css2?family=Open+Sans:wght@400;600;700&display=swap">
<style>
  :root {
    --cherry: #e01f2e;
    --charcoal: #221e1f;
    --paper: #ffffff;
    --backdrop: #ecebe8;
    --ink: #3a3a3a;
  }
  * { margin: 0; padding: 0; box-sizing: border-box; }
  html, body { width: 1200px; height: 900px; overflow: hidden; }
  body {
    background: var(--backdrop);
    font-family: "Open Sans", Arial, sans-serif;
  }
  .sheet {
    width: 1200px; height: 900px;
    display: flex; flex-direction: column;
    align-items: center; justify-content: center; gap: 40px;
  }
  .card {
    width: 700px; height: 400px;
    display: block;
    box-shadow: 0 6px 18px rgba(0,0,0,0.18);
  }
  .fill-cherry { fill: var(--cherry); }
  .fill-charcoal { fill: var(--charcoal); }
  .fill-paper { fill: var(--paper); }
  .company-name { fill: var(--paper); font-weight: 700; font-size: 34px; }
  .address { fill: var(--paper); font-weight: 400; font-size: 19px; }
  .person-name { fill: var(--paper); font-weight: 600; font-size: 24px; letter-spacing: 0.5px; }
  .person-role { fill: var(--cherry); font-weight: 400; font-size: 19px; }
  .contact { fill: var(--ink); font-weight: 400; font-size: 18px; }
  .rule { stroke: var(--cherry); stroke-width: 1.5; }
  .divider { stroke: var(--paper); stroke-width: 6; fill: none; }
  .icon { fill: none; stroke: var(--cherry); stroke-width: 1.4; }
</style>
</head>
<body>
<main class="sheet">

  <!-- Card front -->
  <svg class="card card-front" viewBox="0 0 700 400" xmlns="http://www.w3.org/2000/svg">
    <rect class="fill-cherry" width="700" height="400"/>
    <polygon class="fill-charcoal" points="60,400 235,175 560,175 700,55 700,400"/>
    <g class="brand">
      <rect class="fill-paper" x="118" y="118" width="22" height="22"/>
      <text class="company-name" x="152" y="141">Varno Tolt Hire Pty Ltd</text>
    </g>
    <g class="location">
      <g class="pin" transform="translate(420,240)">
        <circle cx="0" cy="0" r="13" fill="none" stroke="#fff" stroke-width="1.6"/>
        <path d="M0,-7 a5,5 0 0 1 5,5 c0,4 -5,9 -5,9 c0,0 -5,-5 -5,-9 a5,5 0 0 1 5,-5z" fill="#fff"/>
        <circle cx="0" cy="-2" r="1.8" fill="var(--charcoal)"/>
      </g>
      <text class="address" x="420" y="290" text-anchor="middle">218-224 Dunmore Road, Yarraville</text>
    </g>
  </svg>

  <!-- Card back -->
  <svg class="card card-back" viewBox="0 0 700 400" xmlns="http://www.w3.org/2000/svg">
    <rect class="fill-paper" width="700" height="400"/>
    <polygon class="fill-cherry" points="350,0 700,0 700,250 315,190"/>
    <polygon class="fill-charcoal" points="0,0 345,0 310,190 215,400 0,400"/>
    <polyline class="divider" points="348,0 312,190 215,400"/>
    <line class="divider" x1="312" y1="190" x2="700" y2="252"/>

    <g class="brand">
      <rect class="fill-paper" x="440" y="72" width="18" height="18"/>
      <text class="company-name" x="466" y="90" style="font-size:24px">Varno Tolt Hire</text>
      <text class="company-name" x="466" y="120" style="font-size:24px">Pty Ltd</text>
    </g>

    <g class="identity">
      <text class="person-name" x="40" y="318">ROS PENBURY</text>
      <text class="person-role" x="40" y="345">director</text>
    </g>

    <g class="contacts">
      <circle class="icon" cx="290" cy="293" r="7"/>
      <path d="M287,290 l2,-1 l1,3 l-1,1 q1,2 3,3 l1,-1 l3,1 l-1,2 q-5,0 -8,-8z" fill="var(--cherry)"/>
      <text class="contact" x="310" y="299">03 9412 5038</text>
      <circle class="icon" cx="290" cy="320" r="7"/>
      <rect x="287.5" y="315" width="5" height="10" rx="1" fill="var(--cherry)"/>
      <text class="contact" x="310" y="326">0427 836 207</text>
      <line class="rule" x1="270" y1="340" x2="670" y2="340"/>

      <circle class="icon" cx="290" cy="360" r="7"/>
      <rect x="286" y="357" width="8" height="6" fill="none" stroke="var(--cherry)" stroke-width="1.2"/>
      <text class="contact" x="310" y="366">ros.penbury@varnotolt-example.com.au</text>
      <circle class="icon" cx="290" cy="385" r="7"/>
      <line x1="283" y1="385" x2="297" y2="385" stroke="var(--cherry)" stroke-width="1.2"/>
      <text class="contact" x="310" y="391">www.varnotolt-example.com.au</text>
    </g>
  </svg>

</main>
</body>
</html>
```